A4 sized 'product advertisement'

Require a A4 Sized advertisement to promote a new product.

File must be provided in .psd format, unflattened, unmerged as the specifics of the item advertised will be decided at a later date.

Add must include:
- logo
- business name, address, phone number, website and email address
- area for product name
- area for product dimension
- area for product cost
- area for product photo
- document be suitable with the correct 'bleed' for printing
- include a border

I have attached Logo in .psd format.
Design can be in website contrast - or can be completely different. (will consider new 'exciting' ideas)
Updates

TEMPLATE IS NOT TO USE PICTURES FROM THE WEBSITE - AND IS ONLY TO PROMOTE ONE ITEM NOT MULTIPLE.

Industry/Entity Type

Trade

Requirements
Must have
• - be simple, yet eye catching.
• - easy to read.

```html
<!DOCTYPE html>
<html lang="en">
<head>
<meta charset="utf-8">
<title>Barwick Timber – Product Flyer</title>
<link rel="stylesheet" href="https://fonts.googleapis.com/css2?family=Open+Sans:wght@700&family=Oswald:wght@700&family=Lato:wght@400;700&display=swap">
<style>
  :root{
    --brand-blue:#0b4a7f;
    --footer-blue:#0d5696;
    --header-grey:#dcdcdc;
    --photo-grey:#cbcbcb;
    --ink:#1b1b1b;
    --page-bg:#ecebe8;
    --paper:#ffffff;
  }
  *{margin:0;padding:0;box-sizing:border-box}
  html,body{width:1200px;height:1200px;overflow:hidden;background:var(--page-bg)}
  .flyer{position:absolute;left:197px;top:30px;width:806px;height:1138px;background:var(--paper);overflow:hidden;box-shadow:0 2px 10px rgba(0,0,0,.18);font-family:'Lato',sans-serif}
  .hero{position:absolute;left:0;top:0;width:100%;height:420px;background:var(--header-grey)}
  .brand{position:absolute;left:40px;top:78px;display:flex;align-items:center;gap:10px;font-family:'Open Sans',sans-serif;font-weight:700;font-size:30px;color:var(--brand-blue);letter-spacing:.5px}
  .brand-mark{width:22px;height:22px;background:var(--brand-blue)}
  .tagline{position:absolute;left:35px;top:176px;color:var(--brand-blue)}
  .tagline-lead{font-family:'Open Sans',sans-serif;font-weight:700;font-size:31px;line-height:40px;display:block}
  .tagline-main{font-family:'Oswald',sans-serif;font-weight:700;font-size:35px;line-height:42px;display:block;letter-spacing:-.3px}
  .range{position:absolute;top:285px;list-style:none;font-family:'Open Sans',sans-serif;font-weight:700;font-size:18px;line-height:24.5px;color:var(--ink)}
  .range li::before{content:"•";margin-right:5px}
  .range-a{left:35px}
  .range-b{left:205px}
  .name-band{position:absolute;left:0;top:420px;width:806px;height:70px}
  .product-name{position:absolute;left:36px;top:438px;color:#fff;font-weight:700;font-size:24px;letter-spacing:.3px}
  .product-photo{position:absolute;left:37px;top:546px;width:310px;height:457px;background:var(--photo-grey);border:3px solid var(--brand-blue);border-radius:8px}
  .price-table{position:absolute;left:410px;top:554px;width:370px;border-collapse:collapse}
  .price-table th{font-weight:700;font-size:24.5px;color:var(--brand-blue);text-align:left;height:34px;vertical-align:top}
  .price-table td{font-size:19px;color:var(--ink);height:27px;line-height:27px}
  .price-table .dim{padding-left:23px;position:relative;width:263px}
  .price-table .dim::before{content:"";position:absolute;left:3px;top:11px;width:6px;height:6px;border-radius:50%;background:var(--brand-blue)}
  .footer-rule{position:absolute;left:0;top:1056px;width:806px;height:7px;background:var(--brand-blue)}
  .footer{position:absolute;left:0;top:1066px;width:806px;height:72px;background:linear-gradient(90deg,#0a4a82,var(--footer-blue) 50%,#0a4a82);color:#fff;font-size:12.5px;line-height:15px}
  .contact{position:absolute;display:flex;gap:8px}
  .contact svg{flex:none;width:17px;height:17px;fill:#fff}
  .contact strong{font-weight:700}
  .c-address{left:37px;top:10px}
  .c-phone{left:307px;top:12px;align-items:center}
  .c-mail{left:307px;top:38px;align-items:center}
  .c-web{left:583px;top:18px}
  .c-web div{line-height:24px;margin-top:-4px}
</style>
</head>
<body>
<main class="flyer">
  <section class="hero">
    <div class="brand"><span class="brand-mark"></span>BARWICK TIMBER</div>
    <h1 class="tagline"><span class="tagline-lead">Supplying</span><span class="tagline-main">Top Quality Materials</span></h1>
    <ul class="range range-a"><li>125X75 Posts</li><li>75X50 Rails</li><li>150X25 Plinth</li></ul>
    <ul class="range range-b"><li>Palings</li><li>Fence Capping</li><li>Sleepers</li></ul>
  </section>

  <svg class="name-band" viewBox="0 0 806 70" aria-hidden="true">
    <path d="M0 0H806V24H320Q310 24 305 33L289 60Q284 67 274 67H0Z" fill="#0b4a7f"/>
  </svg>
  <h2 class="product-name">PRODUCT NAME</h2>

  <div class="product-photo" role="img" aria-label="Product photo area"></div>

  <table class="price-table">
    <thead><tr><th>Dimension</th><th>COST</th></tr></thead>
    <tbody>
      <tr><td class="dim">00X000X000</td><td>$ 00000.00</td></tr>
      <tr><td class="dim">00X000X000</td><td>$ 00000.00</td></tr>
      <tr><td class="dim">00X000X000</td><td>$ 00000.00</td></tr>
      <tr><td class="dim">00X000X000</td><td>$ 00000.00</td></tr>
      <tr><td class="dim">00X000X000</td><td>$ 00000.00</td></tr>
      <tr><td class="dim">00X000X000</td><td>$ 00000.00</td></tr>
      <tr><td class="dim">00X000X000</td><td>$ 00000.00</td></tr>
      <tr><td class="dim">00X000X000</td><td>$ 00000.00</td></tr>
      <tr><td class="dim">00X000X000</td><td>$ 00000.00</td></tr>
      <tr><td class="dim">00X000X000</td><td>$ 00000.00</td></tr>
      <tr><td class="dim">00X000X000</td><td>$ 00000.00</td></tr>
      <tr><td class="dim">00X000X000</td><td>$ 00000.00</td></tr>
      <tr><td class="dim">00X000X000</td><td>$ 00000.00</td></tr>
      <tr><td class="dim">00X000X000</td><td>$ 00000.00</td></tr>
      <tr><td class="dim">00X000X000</td><td>$ 00000.00</td></tr>
      <tr><td class="dim">00X000X000</td><td>$ 00000.00</td></tr>
    </tbody>
  </table>

  <div class="footer-rule" aria-hidden="true"></div>

  <footer class="footer">
    <div class="contact c-address">
      <svg viewBox="0 0 16 16"><path d="M8 1 0 8h2v7h4v-4h4v4h4V8h2z"/></svg>
      <div><strong>BARWICK TIMBER</strong><br>12 Ridgeline Road,<br>Fernvale VIC 3990</div>
    </div>
    <div class="contact c-phone">
      <svg viewBox="0 0 16 16"><path d="M1 3h3v11H1zM5 2h10v13H5zm2 2v3h6V4zm0 5v1.5h1.5V9zm2.5 0v1.5H11V9zM12 9v1.5h1.5V9zM7 11.5V13h1.5v-1.5zm2.5 0V13H11v-1.5zm2.5 0V13h1.5v-1.5z"/></svg>
      <span>03 9000-1234</span>
    </div>
    <div class="contact c-mail">
      <svg viewBox="0 0 16 16"><path d="M1 4h14v10H1zm1.5 1.2L8 9.5l5.5-4.3z"/></svg>
      <span>info@barwicktimber.com</span>
    </div>
    <div class="contact c-web">
      <svg viewBox="0 0 16 16"><path d="M8 1a7 7 0 1 0 0 14A7 7 0 0 0 8 1zm0 1.5c.8 0 1.9 2 2.1 4.7H5.9C6.1 4.5 7.2 2.5 8 2.5zM4.4 7.2H2.6a5.5 5.5 0 0 1 3.3-4.3 9 9 0 0 0-1.5 4.3zm0 1.6a9 9 0 0 0 1.5 4.3 5.5 5.5 0 0 1-3.3-4.3zm1.5 0h4.2c-.2 2.7-1.3 4.7-2.1 4.7s-1.9-2-2.1-4.7zm5.7 0h1.8a5.5 5.5 0 0 1-3.3 4.3 9 9 0 0 0 1.5-4.3zm0-1.6a9 9 0 0 0-1.5-4.3 5.5 5.5 0 0 1 3.3 4.3z"/></svg>
      <div>barwicktimber.com.au<br>barwicktimbersupplies.com.au</div>
    </div>
  </footer>
</main>
</body>
</html>
```